Selvin: A Friday night in the Prophetic Flyer

We are holding 2 Friday night events, one on 10/25/19 and the other on 11/29/19.
The time frame is 6:30pm-9:00pm. These services will be a time of prayer/healing for the sick and will be prophetic as well. (There will be prophets prophesying over people)

The event is called: Selvin: A Friday night in the Prophetic
The flyer should also include the phrase/excerpt: "And they prophesied also".

Keywords/Phrases: Prophetic, Healing, Climbing in the Spirit, Higher level of Anointing...

Target Market(s)

those looking for healing, seeking a word from God

Colors

Designer to choose colors to be used in the design.

Requirements
Must have
• The event is called: Selvin: A Friday night in the Prophetic
• The flyer should also include the phrase/excerpt: "And they prophesied also".
• It must include the Tovik logo attached, either is fine, we have attached two different versions.
• It must have the dates, location, time
• Dates: October 25, 2019 and November 29, 2019
• Location: Hollard Community Center
• (Downtown Portland) 482 Wendle Street
• Portland, ME 04102
• Time: 6:30pm-9:00pm
• Contact Info: Tel. 207-555-3841
• email: contact@brimfield-hall.org
• web: www.tovik.org
Nice to have
• creativity in color scheme, the meaning of the word Selvin conveyed in a classy artistic way/design.
Should not have
• Crosses, pictures of churches

```html
<!DOCTYPE html>
<html lang="en">
<head>
<meta charset="utf-8">
<title>Selvin: A Friday night in the Prophetic</title>
<link rel="stylesheet" href="https://fonts.googleapis.com/css2?family=Kaushan+Script&family=Roboto+Condensed:wght@400;700&display=swap">
<style>
  :root {
    --page: #ffffff;
    --night: #1d2120;
    --olive: #4a4630;
    --glow: #f0a46a;
    --amber: #f39a1e;
    --white: #ffffff;
  }
  * { margin: 0; padding: 0; box-sizing: border-box; }
  html, body { width: 966px; height: 1200px; overflow: hidden; background: var(--page); }
  .flyer { position: relative; width: 966px; height: 1200px; font-family: "Roboto Condensed", "Arial Narrow", Arial, sans-serif; }
  .hero-photo {
    position: absolute; left: 75px; top: 72px; width: 816px; height: 1056px;
    background:
      radial-gradient(ellipse 230px 360px at 700px 330px, rgba(240,164,106,.85), rgba(240,164,106,.25) 60%, transparent 100%),
      radial-gradient(ellipse 160px 260px at 760px 620px, rgba(214,150,110,.6), transparent 100%),
      radial-gradient(ellipse 90px 300px at 790px 960px, rgba(80,92,110,.8), transparent 100%),
      linear-gradient(180deg, var(--olive) 0%, #2c2d24 40%, var(--night) 75%, #181c1c 100%);
  }
  .content { position: absolute; inset: 0; color: var(--white); }
  .event-title { position: absolute; left: 160px; top: 188px; font-family: "Kaushan Script", "Yellowtail", "Brush Script MT", cursive; font-size: 140px; line-height: 1.1; font-weight: 400; }
  .event-subtitle { position: absolute; left: 161px; top: 374px; font-size: 31px; font-weight: 700; color: var(--amber); }
  .scripture { position: absolute; left: 205px; top: 424px; font-size: 23px; font-weight: 700; letter-spacing: .3px; }
  .dates { position: absolute; left: 162px; top: 580px; font-size: 42px; font-weight: 700; line-height: 50px; letter-spacing: .3px; }
  .time { position: absolute; left: 163px; top: 686px; font-size: 24px; font-weight: 700; color: var(--amber); }
  .venue-name { position: absolute; left: 158px; top: 740px; font-size: 42px; font-weight: 700; color: var(--amber); letter-spacing: .3px; }
  .venue-address { position: absolute; left: 158px; top: 792px; font-size: 26px; font-weight: 700; line-height: 34px; letter-spacing: .4px; }
  .org-mark { position: absolute; left: 130px; top: 985px; display: flex; align-items: center; gap: 14px; }
  .org-mark .dot { width: 26px; height: 26px; border-radius: 50%; background: var(--amber); }
  .org-mark .name { font-size: 58px; font-weight: 400; color: var(--white); letter-spacing: 1px; }
  .divider { position: absolute; left: 366px; top: 968px; width: 2px; height: 108px; background: var(--white); }
  .phone { position: absolute; left: 390px; top: 982px; font-size: 38px; font-weight: 700; color: var(--amber); }
  .contact-line { position: absolute; left: 390px; top: 1034px; font-size: 20px; font-weight: 700; }
  .contact-line .web { margin-left: 20px; }
</style>
</head>
<body>
  <main class="flyer">
    <div class="hero-photo" role="img" aria-label="Photograph of an open hand raised in warm glowing light against a dark background"></div>
    <div class="content">
      <h1 class="event-title">Selvin</h1>
      <p class="event-subtitle">A Friday night in the Prophetic</p>
      <p class="scripture">“And they prophesied also”</p>
      <p class="dates">October 25 &amp;<br>November 29, 2019</p>
      <p class="time">6:30pm – 9:00pm</p>
      <p class="venue-name">Hollard Community Center</p>
      <p class="venue-address">(Downtown Portland) 482 Wendle Street<br>Portland, ME 04102</p>
      <div class="org-mark"><span class="dot"></span><span class="name">TOVIK</span></div>
      <div class="divider"></div>
      <p class="phone">207-555-3841</p>
      <p class="contact-line"><span class="email">contact@brimfield-hall.org</span><span class="web">www.tovik.org</span></p>
    </div>
  </main>
</body>
</html>
```